Building and Maintenance Company requires a flyer design, Specialising in domestic and commercial bu

We need a flyer design for a company based in Melbourne Victoria, we want to send the flyer out to businesses to obtain more work.

KEL Building and Construction provides the solution for all your building and maintenance needs

We have a professional and highly regarded team of reliable and skilled tradesmen who specialise in building services, domestic and commercial maintenance and gardening in Victoria and Tasmania.

Include our contact details;
0407 318 624
info@kelbuilding.com.au
www.kelbuilding.com.au

Target Market(s)

Domestic and Commercial Clients looking for building maintenance, window cleaning or gardening

Industry/Entity Type

It Company

Font styles to use
Sans Serif

Colors
33b8a4
474747
ffffff

Requirements
Must have
• Images and colour
Nice to have
• We would like the flyer to have our contact details on it.
• Colourful
• Clearly explains what we do, which is, 'KEL Building and Construction provides the solution for all your building, maintenance and gardening needs.'

```html
<!DOCTYPE html>
<html lang="en">
<head>
<meta charset="UTF-8">
<title>KEL Building and Construction – Flyer</title>
<link href="https://fonts.googleapis.com/css2?family=Archivo+Black&family=Lato:wght@400;700&display=swap" rel="stylesheet">
<style>
  :root {
    --teal: #33b8a4;
    --teal-light: #45c9b2;
    --teal-dark: #1f7f70;
    --charcoal: #474747;
    --ink: #2e2e2e;
    --white: #ffffff;
    --paper-hi: #f7f7f7;
    --paper-lo: #e4e4e4;
    --lime: #7dff1e;
    --stage: #141414;
    --rope: #c9a24a;
  }
  * { box-sizing: border-box; margin: 0; padding: 0; }
  html, body { width: 1200px; height: 840px; overflow: hidden; }
  body {
    background: var(--stage);
    font-family: "Lato", Arial, sans-serif;
    position: relative;
  }
  .flyer {
    position: absolute;
    left: 340px; top: 46px;
    width: 530px; height: 748px;
    background: linear-gradient(160deg, var(--paper-hi) 0%, var(--paper-lo) 55%, var(--paper-hi) 100%);
    overflow: hidden;
    box-shadow: 0 18px 40px rgba(0,0,0,.5);
  }
  .hero-disc { position: absolute; left: 90px; top: -230px; width: 520px; height: 520px; }
  .ropes { position: absolute; inset: 0; width: 530px; height: 748px; }
  .headline {
    position: absolute; left: 170px; top: 48px; width: 330px;
    text-align: center;
    font-family: "Archivo Black", "Arial Black", sans-serif;
    line-height: 1.05;
  }
  .headline .lead { color: var(--lime); font-size: 24px; display: block; margin-bottom: 6px; }
  .headline .main { color: var(--white); font-size: 31px; display: block; }
  .photo {
    position: absolute; width: 148px; height: 118px;
    border: 5px solid var(--charcoal); border-radius: 8px;
    box-shadow: 0 10px 16px rgba(0,0,0,.35);
  }
  .photo--mowing { left: 62px; top: 240px; background: linear-gradient(180deg, #a9b7c4 0%, #6d7a6f 40%, #4f8f2c 60%, #3d7a22 100%); }
  .photo--lawn { left: 195px; top: 320px; background: linear-gradient(180deg, #b83a33 0%, #3f7c22 40%, #6fc23a 100%); }
  .photo--facade { left: 335px; top: 345px; background: linear-gradient(160deg, #8a8f99 0%, #b9bcc2 45%, #d9a52a 70%, #8c8f94 100%); }
  .brand {
    position: absolute; left: 30px; top: 452px;
    color: var(--charcoal); font-weight: 700;
  }
  .brand-name { display: block; font-size: 19px; line-height: 1.15; letter-spacing: .5px; text-transform: uppercase; }
  .brand-name b { display: block; font-size: 44px; letter-spacing: 2px; line-height: 1; }
  .rule { position: absolute; left: 0; height: 3px; background: var(--teal); }
  .rule--top { top: 560px; width: 250px; }
  .rule--bottom { top: 718px; width: 530px; }
  .phone {
    position: absolute; left: 30px; top: 578px;
    display: flex; align-items: center; gap: 10px;
    color: var(--teal); font-size: 30px; font-weight: 700; letter-spacing: 1px;
  }
  .phone svg { width: 26px; height: 26px; }
  .about {
    position: absolute; left: 272px; top: 490px; width: 228px;
    font-size: 12.5px; line-height: 1.3; color: var(--ink);
    text-align: justify; text-indent: 22px;
    z-index: 2;
  }
  .grass {
    position: absolute; left: 210px; top: 600px; width: 320px; height: 70px;
    background: linear-gradient(180deg, rgba(125,200,60,0) 0%, #6cc23a 50%, #3f8f22 100%);
    z-index: 1;
  }
  .contact {
    position: absolute; right: 24px; top: 678px;
    text-align: right; font-size: 11.5px; color: var(--ink); line-height: 1.35;
    font-style: normal;
  }
</style>
</head>
<body>
  <main class="flyer">
    <svg class="hero-disc" viewBox="0 0 520 520" aria-hidden="true">
      <circle cx="260" cy="260" r="258" fill="var(--teal-dark)"/>
      <circle cx="270" cy="250" r="240" fill="var(--teal)"/>
      <circle cx="290" cy="230" r="200" fill="var(--teal-light)" opacity=".45"/>
    </svg>

    <svg class="ropes" viewBox="0 0 530 748" aria-hidden="true">
      <line x1="136" y1="200" x2="136" y2="242" stroke="var(--rope)" stroke-width="4" stroke-dasharray="5 3"/>
      <line x1="268" y1="280" x2="268" y2="322" stroke="var(--rope)" stroke-width="4" stroke-dasharray="5 3"/>
      <line x1="410" y1="288" x2="410" y2="347" stroke="var(--rope)" stroke-width="4" stroke-dasharray="5 3"/>
    </svg>

    <h1 class="headline">
      <span class="lead">provides the solution for</span>
      <span class="main">all your building and maintenance needs</span>
    </h1>

    <div class="photo photo--mowing" role="img" aria-label="Photo of a ride-on mower cutting a front lawn"></div>
    <div class="photo photo--lawn" role="img" aria-label="Close-up photo of a mower wheel on fresh grass"></div>
    <div class="photo photo--facade" role="img" aria-label="Photo of abseiling workers cleaning a building facade"></div>

    <div class="brand">
      <span class="brand-name"><b>KEL</b>Building and<br>Construction</span>
    </div>

    <div class="rule rule--top"></div>

    <div class="phone">
      <svg viewBox="0 0 26 26" aria-hidden="true">
        <circle cx="13" cy="13" r="13" fill="var(--teal)"/>
        <path d="M9.2 6.5c.5-.3 1.1-.2 1.4.3l1.2 2c.3.5.2 1-.2 1.4l-.8.7c.6 1.4 1.7 2.6 3.1 3.3l.7-.8c.4-.4 1-.5 1.4-.2l2 1.2c.5.3.6.9.3 1.4l-.8 1.2c-.5.7-1.4 1-2.2.8-3.5-1-6.3-3.8-7.3-7.3-.2-.8.1-1.7.8-2.2z" fill="var(--white)"/>
      </svg>
      <span>0407 318 624</span>
    </div>

    <div class="grass" role="img" aria-label="Illustration of green grass blades"></div>

    <p class="about">We have a professional and highly regarded team of reliable and skilled tradesmen who specialise in building services, domestic and commercial maintenance and gardening in Victoria and Tasmania.</p>

    <address class="contact">
      info@kelbuilding.com.au<br>
      www.kelbuilding.com.au
    </address>

    <div class="rule rule--bottom"></div>
  </main>
</body>
</html>
```